Web Design Project for lawn care business

after having a logo designed now my website is letting me down.
My websites main purpose is once i have made contact with a customer most will then try to research my company and the work i have done. Going to my unprofessional and untidy site will only put off potential customers. Also some customers will find my site online so must be able to grab their attention.

My site must be in keeping with my logo. Which is modern, sleek and classy. It needs to convey how professional we are and that the customer is getting a professional service.

My existing site will be replaced with the winning design.

Content wise and amount of pages will be similar to mine how ever more data will be inputted by myself.

so far prefer sites designed incorporating links in pictures or animated links to flick through pictures etc

breaks up the site and is more user friendly. 

also need to make sure colours are in keeping with logo or at least have similarities to keep it all uniform.

thanks

Lawn Care

• in keeping font wise with my logo
same colours etc

```html
<!DOCTYPE html>
<html lang="en">
<head>
<meta charset="utf-8">
<title>Fairway Lawn Care</title>
<link rel="stylesheet" href="https://fonts.googleapis.com/css2?family=Cinzel:wght@400;700&family=Abel&family=Open+Sans:wght@400;700&display=swap">
<style>
:root{
  --black:#000;
  --lime:#9fdc2e;
  --lime-soft:#b6e05a;
  --leaf:#3f5c1f;
  --leaf-dark:#2f4719;
  --forest:#1d2e0e;
  --brown:#5a3512;
  --brown-dark:#2e1a06;
  --white:#fff;
  --grey:#cfcfcf;
}
*{margin:0;padding:0;box-sizing:border-box}
html,body{width:852px;height:1200px;overflow:hidden;background:var(--black)}
body{position:relative;font-family:"Open Sans",sans-serif;color:var(--white)}
.abs{position:absolute}

.brand{left:40px;top:66px;width:300px}
.brand-name{font-family:"Cinzel",serif;font-weight:400;color:var(--lime-soft);font-size:26px;line-height:30px;display:flex;align-items:center;gap:10px;white-space:nowrap}
.brand-dot{width:14px;height:14px;border-radius:50%;background:var(--lime-soft);flex:none}

.contact{top:52px;font-family:"Abel",sans-serif;font-size:22px;color:var(--lime);display:flex;align-items:center;gap:10px;white-space:nowrap}
.contact.phone{left:355px}
.contact.email{left:555px}

.hero{left:58px;top:125px;width:542px;height:247px;background:radial-gradient(ellipse at 40% 50%,#a6e04a 0%,#6fbf1f 40%,#2f7a0d 100%);border:1px solid #4d7a20}
.quote-banner{left:50px;top:322px;width:321px;height:36px;background:rgba(70,40,10,.85);font-family:"Cinzel",serif;font-size:18px;line-height:36px;padding-left:41px;color:var(--white)}
.hero-dots{left:534px;top:354px;display:flex;gap:8px}
.hero-dots span{width:8px;height:8px;border-radius:50%;background:rgba(255,255,255,.6)}

.commitment{left:616px;top:120px}
.commitment h2{font-family:"Cinzel",serif;font-weight:400;font-size:18px;color:var(--lime);letter-spacing:.5px;margin-bottom:22px}
.commitment li{list-style:none;font-family:"Abel",sans-serif;font-size:15px;height:46.5px;display:flex;align-items:flex-start;gap:4px}
.commitment li::before{content:"";width:13px;height:13px;background:var(--brown);margin-top:3px}

.services-band{left:0;top:378px;width:852px;height:192px;background:linear-gradient(#000 0%,#0e1707 35%,#2a4014 100%);border-bottom:3px solid #5a9a1a}
.thread{top:395px;width:1px;height:195px;background:#8a8a8a;z-index:2}
.pin{top:586px;width:16px;height:16px;border-radius:50%;background:radial-gradient(circle,#111 30%,#777 45%,#222 80%);z-index:3}
.service{top:417px;width:170px;text-align:center}
.service-icon{width:68px;height:68px;border-radius:50%;background:#3c5a1c;margin:0 auto 13px;display:flex;align-items:center;justify-content:center}
.service-title{font-family:"Cinzel",serif;font-weight:700;font-size:15px;color:var(--lime-soft);letter-spacing:.3px}

.content{left:0;top:580px;width:852px;height:396px;background:var(--leaf)}
.why{left:40px;top:631px;width:412px;height:313px;background:var(--leaf-dark);padding:12px 10px}
.why h2{font-family:"Cinzel",serif;font-weight:400;font-size:26px;color:var(--lime);text-align:center;margin-bottom:12px}
.why-cols{display:flex;gap:10px}
.why-cols p{width:196px;font-size:10.2px;line-height:13px}
.garden-photo{left:510px;top:632px;width:265px;height:312px;background:linear-gradient(160deg,#4f7d2a 0%,#5f9a30 60%,#487a24 100%)}

.rule{left:0;top:984px;width:852px;height:6px;background:var(--brown-dark)}
.footer-brand{left:60px;top:1040px;width:240px}
.footer-brand .brand-name{font-size:20px;line-height:24px}
.footer h3{font-family:"Open Sans",sans-serif;font-size:9px;font-weight:700;position:absolute}
.gallery{left:333px;top:1033px;display:grid;grid-template-columns:repeat(3,46px);gap:16px}
.thumb{width:46px;height:46px;border:2px solid var(--grey)}
.tweets{left:581px;top:1034px;width:180px;font-size:10px;line-height:13px}
.tweets .handle,.tweets .link{color:var(--lime)}
.tweets time{display:block;font-size:8px;margin:6px 0 12px}
.copyright{left:0;top:1185px;width:852px;height:15px;background:var(--forest);font-size:7px;text-align:center;line-height:15px;color:#0a0a0a;letter-spacing:.3px}
</style>
</head>
<body>

<header>
  <div class="abs brand"><div class="brand-name"><span class="brand-dot"></span>Fairway Lawn Care</div></div>
  <div class="abs contact phone">
    <svg width="20" height="20" viewBox="0 0 24 24" aria-hidden="true"><path fill="#9fdc2e" d="M6.6 10.8a15 15 0 0 0 6.6 6.6l2.2-2.2c.3-.3.7-.4 1-.2 1.1.4 2.3.6 3.6.6.6 0 1 .4 1 1V20c0 .6-.4 1-1 1A17 17 0 0 1 3 4c0-.6.4-1 1-1h3.5c.6 0 1 .4 1 1 0 1.3.2 2.5.6 3.6.1.3 0 .7-.2 1z"/></svg>
    07700 900 418
  </div>
  <div class="abs contact email">
    <svg width="24" height="18" viewBox="0 0 24 18" aria-hidden="true"><rect x="0" y="0" width="24" height="18" fill="#9fdc2e"/><path d="M0 0l12 10L24 0" fill="none" stroke="#000" stroke-width="2"/></svg>
    hello@fairwaylawns.co.uk
  </div>
</header>

<div class="abs hero" role="img" aria-label="Close-up photograph of fresh green grass blades"></div>
<div class="abs quote-banner">Get A Free Quote Today!</div>
<div class="abs hero-dots"><span></span><span></span><span></span><span></span></div>

<section class="abs commitment">
  <h2>Our Commitment</h2>
  <ul>
    <li>Fully Insured</li>
    <li>All Waste Removed</li>
    <li>Qualified Greenkeepers</li>
    <li>Reliable, Prompt &amp; Flexible</li>
    <li>Free No Obligation Quotes</li>
  </ul>
</section>

<section class="services">
  <div class="abs services-band"></div>
  <div class="abs thread" style="left:58px"></div>
  <div class="abs thread" style="left:247px"></div>
  <div class="abs thread" style="left:421px"></div>
  <div class="abs thread" style="left:599px"></div>
  <div class="abs thread" style="left:795px"></div>
  <div class="abs pin" style="left:50px"></div>
  <div class="abs pin" style="left:239px"></div>
  <div class="abs pin" style="left:413px"></div>
  <div class="abs pin" style="left:591px"></div>
  <div class="abs pin" style="left:787px"></div>

  <div class="abs service" style="left:67px">
    <div class="service-icon"><svg width="26" height="26" viewBox="0 0 26 26" aria-hidden="true"><circle cx="13" cy="8" r="5" fill="#fff"/><circle cx="7" cy="15" r="5" fill="#fff"/><circle cx="19" cy="15" r="5" fill="#fff"/><circle cx="13" cy="13" r="2.5" fill="#3c5a1c"/></svg></div>
    <div class="service-title">Garden Services</div>
  </div>
  <div class="abs service" style="left:250px">
    <div class="service-icon"><svg width="24" height="26" viewBox="0 0 24 26" aria-hidden="true"><path d="M12 1l3 6 6-1-3 6 5 3-7 2 1 5-5-3-5 3 1-5-7-2 5-3-3-6 6 1z" fill="#fff"/><rect x="11.3" y="18" width="1.4" height="7" fill="#fff"/></svg></div>
    <div class="service-title">Tree Services</div>
  </div>
  <div class="abs service" style="left:423px">
    <div class="service-icon"><svg width="26" height="26" viewBox="0 0 26 26" aria-hidden="true"><path d="M6 24C6 15 9 8 14 3c-3 7-4 13-4 21zM12 24c1-8 5-13 10-16-4 5-6 10-6 16zM4 24c0-5-1-8-3-11 3 2 5 6 5 11z" fill="#fff"/></svg></div>
    <div class="service-title">Lawn Services</div>
  </div>
  <div class="abs service" style="left:613px">
    <div class="service-icon"><svg width="24" height="24" viewBox="0 0 24 24" aria-hidden="true"><path d="M6 2h12v6a6 6 0 0 1-12 0z" fill="#fff"/><path d="M6 4H2c0 4 2 6 4 6M18 4h4c0 4-2 6-4 6" fill="none" stroke="#fff" stroke-width="1.6"/><rect x="11" y="14" width="2" height="5" fill="#fff"/><rect x="7" y="19" width="10" height="3" fill="#fff"/></svg></div>
    <div class="service-title">Sports Surface</div>
  </div>
</section>

<main>
  <div class="abs content"></div>
  <section class="abs why">
    <h2>WHY CHOOSE US?</h2>
    <div class="why-cols">
      <p>Just as the name suggests all work is carried out by fully qualified Greenkeepers. So why would you want to do it yourself? As Greenkeepers, the meticulous attention to detail and passion that goes into working on a golf course also goes into every <em>other</em> job we do from mowing to full hard landscaping jobs and everything in between. Everyone knows that golf greens are the most immaculate, well maintained and most aesthetically pleasing grassed areas on the planet. With this in mind who else would you want to have maintaining, renovating and constructing your own garden? That's where we come in.</p>
      <p>With access to every piece of equipment, material, chemical and staff needed to maintain a golf course, we are able to offer you the very same services tailored to your garden regardless how big or small and at an affordable price! Costing less than using DIY methods with inefficient materials. Each staff member is fully qualified with a National Diploma in Sportsturf or above, a two year qualification in both practical work and theory. Our staff has a PA1, PA6 &amp; NPTC Spraying certificate which allow us to spray all the chemicals that most gardeners don't have access to. We also hold all relevant NPTC certificates in chainsaw for any arboriculture needs.</p>
    </div>
  </section>
  <div class="abs garden-photo" role="img" aria-label="Photograph of a manicured garden lawn with clipped hedges, topiary and flowers"></div>
</main>

<footer class="footer">
  <div class="abs rule"></div>
  <div class="abs footer-brand"><div class="brand-name"><span class="brand-dot"></span>Fairway Lawn Care</div></div>

  <h3 style="left:333px;top:1010px">GALLERY</h3>
  <div class="abs gallery">
    <div class="thumb" role="img" aria-label="Gallery photo of striped lawn" style="background:#6a9a2a"></div>
    <div class="thumb" role="img" aria-label="Gallery photo of pale grass blades" style="background:#b9d48a"></div>
    <div class="thumb" role="img" aria-label="Gallery photo of dense turf" style="background:#7a9a1e"></div>
    <div class="thumb" role="img" aria-label="Gallery photo of grass close-up" style="background:#3f8a1a"></div>
    <div class="thumb" role="img" aria-label="Gallery photo of lawn pattern" style="background:#7aae32"></div>
    <div class="thumb" role="img" aria-label="Gallery photo of mower on lawn" style="background:#4a6a2a"></div>
  </div>

  <h3 style="left:582px;top:1010px">TWITTER FEED</h3>
  <div class="abs tweets">
    <p>hey <span class="handle">@mossyrake</span> just got my design proofs back from Bluebell Web Studio, so excited!</p>
    <time>1 day ago</time>
    <p>Just purchased <span class="handle">@bluebellweb</span>'s awesome new ebook on owning a website, good read.<br><span class="link">www.bluebellweb.co.uk</span></p>
  </div>

  <div class="abs copyright">COPYRIGHT©2013 FAIRWAY LAWN CARE. ALL RIGHTS RESERVED</div>
</footer>

</body>
</html>
```